Business card for my company-RKV Design Studio

I do not have a logo-I like red and keeping it clean. Information that should be on the card:
Tom Brazenhall AIA
Architecture Planning Interiors
Cell Phone-614.529.4086
email-rkvplanner4@mailvane.net
www.rkvdesignstudio.net

```html
<!DOCTYPE html>
<html lang="en">
<head>
<meta charset="utf-8">
<title>RKV Design Studio – Business Card</title>
<link rel="stylesheet" href="https://fonts.googleapis.com/css2?family=Bodoni+Moda:wght@400;500&family=Montserrat:wght@400&display=swap">
<style>
  :root {
    --page-bg: #e2e2e2;
    --card-bg: #f6f6f6;
    --pattern-tone: #efefef;
    --ink: #161616;
    --accent: #c8202f;
    --rule: #d9a3a8;
    --shadow: rgba(0, 0, 0, 0.18);
  }
  * { margin: 0; padding: 0; box-sizing: border-box; }
  html, body {
    width: 987px;
    height: 1200px;
    overflow: hidden;
    background: var(--page-bg);
  }
  .canvas {
    position: relative;
    width: 987px;
    height: 1200px;
  }
  .card {
    position: absolute;
    left: 74px;
    width: 838px;
    height: 524px;
    background: var(--card-bg);
    box-shadow: 0 1px 3px var(--shadow);
    overflow: hidden;
  }
  .card--front { top: 59px; }
  .card--back  { top: 620px; }

  .card__pattern {
    position: absolute;
    inset: 0;
    background: linear-gradient(180deg, var(--card-bg) 0%, var(--pattern-tone) 50%, var(--card-bg) 100%);
    opacity: 0.6;
  }

  .brand-mark {
    position: absolute;
    display: flex;
    align-items: center;
    justify-content: center;
    gap: 18px;
    color: var(--ink);
    font-family: "Bodoni Moda", serif;
    font-weight: 400;
    white-space: nowrap;
  }
  .brand-mark__square {
    background: var(--accent);
    flex: none;
  }
  .card--front .brand-mark {
    left: 0; right: 0;
    top: 70px;
    height: 130px;
    font-size: 32px;
  }
  .card--front .brand-mark__square { width: 120px; height: 120px; }

  .studio-name {
    position: absolute;
    left: 114px;
    top: 300px;
    font-family: "Bodoni Moda", serif;
    font-weight: 400;
    font-size: 68px;
    line-height: 1;
    color: var(--ink);
    white-space: nowrap;
  }
  .studio-disciplines {
    position: absolute;
    left: 115px;
    top: 381px;
    font-family: "Bodoni Moda", serif;
    font-weight: 400;
    font-size: 39px;
    line-height: 1;
    color: var(--ink);
    white-space: nowrap;
  }

  .person-name {
    position: absolute;
    left: 0; right: 0;
    top: 92px;
    text-align: center;
    font-family: "Bodoni Moda", serif;
    font-weight: 400;
    font-size: 68px;
    line-height: 1;
    color: var(--ink);
    white-space: nowrap;
  }

  .rule {
    position: absolute;
    left: 0; right: 0;
    height: 1px;
    background: var(--rule);
  }
  .rule--upper { top: 242px; }
  .rule--lower { top: 309px; }

  .card--back .brand-mark {
    left: 50%;
    top: 240px;
    transform: translateX(-50%);
    padding: 0 14px;
    height: 72px;
    background: var(--card-bg);
    font-size: 22px;
  }
  .card--back .brand-mark__square { width: 72px; height: 72px; }

  .contact-list {
    position: absolute;
    left: 0; right: 0;
    top: 362px;
    list-style: none;
    text-align: center;
    font-family: "Montserrat", sans-serif;
    font-weight: 400;
    font-size: 23px;
    line-height: 39px;
    color: var(--ink);
  }
</style>
</head>
<body>
<main class="canvas">
  <section class="card card--front">
    <div class="card__pattern" role="img" aria-label="Faint repeating diamond pattern background"></div>
    <div class="brand-mark">
      <span class="brand-mark__square"></span>
      <span class="brand-mark__name">RKV Design Studio</span>
    </div>
    <h1 class="studio-name">RKV Design Studio</h1>
    <p class="studio-disciplines">Architecture Planning Interiors</p>
  </section>

  <section class="card card--back">
    <div class="card__pattern" role="img" aria-label="Faint repeating diamond pattern background"></div>
    <h2 class="person-name">Tom Brazenhall AIA</h2>
    <div class="rule rule--upper"></div>
    <div class="rule rule--lower"></div>
    <div class="brand-mark">
      <span class="brand-mark__square"></span>
      <span class="brand-mark__name">RKV Design Studio</span>
    </div>
    <ul class="contact-list">
      <li>call : 614.529.4086</li>
      <li>email : rkvplanner4@mailvane.net</li>
      <li>website : www.rkvdesignstudio.net</li>
    </ul>
  </section>
</main>
</body>
</html>
```